Label for a tea in a metal box

We need a label for a tea-metal box. The box will be made of silver aluminum. A photo of the metal box is attached. The metal box is together with an infuser (sieve) in a gift box. You can see this in the photo. The label should the dimensions 3.2 cm x 16 cm (total). The label passes through the entire box, is thus glued to the front side, passes over the cover and goes further to the rear and down. We need a coherent area, it is printed in a part. The surface will be split optically into three parts: front, top and back. Warning: The back of course, must be applied in the design rotated by 180 degrees. The top shows in the same direction as the front. The label is printed as a whole and bonded as a whole. This is also from the attached file "feature pattern" seen. In the box of loose Darjeeling Tea will be. The label should look very classy & premium, so minimalist, clean. Not too squashed, not too many different fonts and sizes, just clean, noble and premium. The design should communicate the following values: precious, premium, quality, quality. It should not look too old-fashioned, but also not very hip and trendy. It is indeed modern and vigorous look, but work has also for older customers. You are welcome to work with colors, but please simply, and tea fits as dark green, black, etc. Here is the text that you want on the label and other comments as well as the functional model and a view of the box.
Updates

Target Market(s)

Germany

Requirements
Must have
• The font size must be at least 0.9 mm (based on the small "x")

```html
<!DOCTYPE html>
<html lang="de">
<head>
<meta charset="utf-8">
<title>Darjeeling Premium – Etikettvarianten</title>
<link rel="stylesheet" href="https://fonts.googleapis.com/css2?family=Oswald:wght@300;400;500&display=swap">
<style>
  :root{
    --ink:#111111;
    --paper:#ffffff;
    --frame:#050505;
    --green:#3d7a3a;
    --green-deep:#2f622c;
    --slate:#3a3c37;
    --slate-deep:#262824;
    --rust:#7a3a30;
    --rust-deep:#5a2821;
    --moss:#3f6a2c;
    --moss-deep:#2c4c20;
    --saffron:#c8861f;
    --saffron-deep:#b0591a;
    --crimson:#6e1510;
    --crimson-deep:#2a0707;
    --forest:#1f3a18;
    --forest-deep:#0f1c0b;
  }
  *{box-sizing:border-box;margin:0;padding:0}
  html,body{width:1200px;height:857px;overflow:hidden;background:#000}
  body{font-family:"Oswald",sans-serif;color:var(--ink);-webkit-font-smoothing:antialiased}
  .sheet{display:grid;grid-template-columns:repeat(7,1fr);width:1200px;height:857px}
  .label{position:relative;overflow:hidden}
  .label__surface{position:absolute;inset:0}
  .label--green   .label__surface{background:linear-gradient(180deg,var(--green),var(--green-deep))}
  .label--slate   .label__surface{background:linear-gradient(180deg,var(--slate),var(--slate-deep))}
  .label--rust    .label__surface{background:linear-gradient(180deg,var(--rust),var(--rust-deep))}
  .label--moss    .label__surface{background:linear-gradient(180deg,var(--moss),var(--moss-deep))}
  .label--saffron .label__surface{background:linear-gradient(180deg,var(--saffron),var(--saffron-deep))}
  .label--crimson .label__surface{background:linear-gradient(180deg,var(--crimson),var(--crimson-deep))}
  .label--forest  .label__surface{background:linear-gradient(180deg,var(--forest),var(--forest-deep))}

  .frame{position:absolute;left:17.6px;width:136px;background:var(--frame)}
  .frame--back{top:17.6px;height:298.4px}
  .frame--top{top:352px;height:152px}
  .frame--front{top:540px;height:298.4px}
  .panel{position:absolute;left:14.4px;right:14.4px;top:14.4px;bottom:14.4px;background:var(--paper);text-align:center;color:var(--ink)}
  .panel p,.panel div{color:var(--ink)}

  /* front */
  .front__name{font-weight:400;font-size:26px;line-height:34px;padding-top:11px;letter-spacing:.2px}
  .grade{font-weight:300;font-size:10.5px;line-height:15px}
  .front .grade{margin-top:8px}
  .front__share{font-weight:400;font-size:14px;line-height:19px;margin-top:24px}
  .front__origin{font-weight:300;font-size:10px;line-height:15px;margin-top:4px}
  .front__taste{position:absolute;left:0;right:0;bottom:7px;font-weight:300;font-size:9.6px}

  /* top */
  .top__name{font-weight:400;font-size:17.5px;line-height:20.5px;padding-top:22px}
  .top .grade{margin-top:7px}

  /* back, rotated 180° */
  .back{transform:rotate(180deg)}
  .back > *{position:absolute;left:0;right:0}
  .brew{top:24px;display:flex;justify-content:space-around;padding:0 6px}
  .brew__item{display:flex;flex-direction:column;align-items:center;font-size:6.5px;line-height:8px;font-weight:300;gap:3px}
  .brew__item svg{width:14px;height:14px}
  .back__advice{top:82px;font-weight:300;font-size:9.5px;line-height:19px}
  .back__content{top:130px;font-weight:500;font-size:10.5px;line-height:14px}
  .back__dates{top:193px;font-weight:300;font-size:6.5px;line-height:12px;text-align:left;padding-left:22px}
  .back__maker{top:241px;font-weight:300;font-size:5px;line-height:8px}
</style>
</head>
<body>
<main class="sheet">

<section class="label label--green">
  <div class="label__surface" role="img" aria-label="Green textured background surface"></div>
  <div class="frame frame--back"><div class="panel back">
    <div class="brew">
      <div class="brew__item"><svg viewBox="0 0 14 14"><circle cx="7" cy="7" r="6" fill="none" stroke="#111" stroke-width="1.2"/><path d="M7 3v4l2 2" fill="none" stroke="#111" stroke-width="1.2"/></svg>3 - 4 Min.</div>
      <div class="brew__item"><svg viewBox="0 0 14 14"><path d="M2 6h9v3a3 3 0 0 1-3 3H5a3 3 0 0 1-3-3z M11 7h1.5v2H11" fill="none" stroke="#111" stroke-width="1.1"/><path d="M5 2v2M8 2v2" stroke="#111" stroke-width="1"/></svg>100°C</div>
      <div class="brew__item"><svg viewBox="0 0 14 14"><ellipse cx="4.5" cy="5" rx="3" ry="2.4" fill="none" stroke="#111" stroke-width="1.1"/><path d="M7 6.5l6 5" stroke="#111" stroke-width="1.3"/></svg>1½ Teesieb</div>
    </div>
    <p class="back__advice">Für optimalen Geschmack<br>weiches Wasser verwenden.</p>
    <p class="back__content">Inhalt: 20g</p>
    <p class="back__dates">Mindestens haltbar bis:<br>Charge:</p>
    <p class="back__maker">Exklusiv für die Teekiste<br>ausgewählt von Teehaus Morgen GmbH<br>Birkenweg 12, D-20000 Hamburg</p>
  </div></div>
  <div class="frame frame--top"><div class="panel top"><p class="top__name">Darjeeling<br>Premium</p><p class="grade">FTGFOP 1<br>First Flush</p></div></div>
  <div class="frame frame--front"><div class="panel front"><p class="front__name">Darjeeling<br>Premium</p><p class="grade">FTGFOP 1<br>First Flush</p><p class="front__share">100 %<br>Schwarzer Tee</p><p class="front__origin">Lindgar Farm im<br>indischen Himalaya</p><p class="front__taste">fein, aromatisch &amp; blumig</p></div></div>
</section>

<section class="label label--slate">
  <div class="label__surface" role="img" aria-label="Decorative pattern area in charcoal and grey"></div>
  <div class="frame frame--back"><div class="panel back">
    <div class="brew">
      <div class="brew__item"><svg viewBox="0 0 14 14"><circle cx="7" cy="7" r="6" fill="none" stroke="#111" stroke-width="1.2"/><path d="M7 3v4l2 2" fill="none" stroke="#111" stroke-width="1.2"/></svg>3 - 4 Min.</div>
      <div class="brew__item"><svg viewBox="0 0 14 14"><path d="M2 6h9v3a3 3 0 0 1-3 3H5a3 3 0 0 1-3-3z M11 7h1.5v2H11" fill="none" stroke="#111" stroke-width="1.1"/><path d="M5 2v2M8 2v2" stroke="#111" stroke-width="1"/></svg>100°C</div>
      <div class="brew__item"><svg viewBox="0 0 14 14"><ellipse cx="4.5" cy="5" rx="3" ry="2.4" fill="none" stroke="#111" stroke-width="1.1"/><path d="M7 6.5l6 5" stroke="#111" stroke-width="1.3"/></svg>1½ Teesieb</div>
    </div>
    <p class="back__advice">Für optimalen Geschmack<br>weiches Wasser verwenden.</p>
    <p class="back__content">Inhalt: 20g</p>
    <p class="back__dates">Mindestens haltbar bis:<br>Charge:</p>
    <p class="back__maker">Exklusiv für die Teekiste<br>ausgewählt von Teehaus Morgen GmbH<br>Birkenweg 12, D-20000 Hamburg</p>
  </div></div>
  <div class="frame frame--top"><div class="panel top"><p class="top__name">Darjeeling<br>Premium</p><p class="grade">FTGFOP 1<br>First Flush</p></div></div>
  <div class="frame frame--front"><div class="panel front"><p class="front__name">Darjeeling<br>Premium</p><p class="grade">FTGFOP 1<br>First Flush</p><p class="front__share">100 %<br>Schwarzer Tee</p><p class="front__origin">Lindgar Farm im<br>indischen Himalaya</p><p class="front__taste">fein, aromatisch &amp; blumig</p></div></div>
</section>

<section class="label label--rust">
  <div class="label__surface" role="img" aria-label="Decorative pattern area in rust red and brown"></div>
  <div class="frame frame--back"><div class="panel back">
    <div class="brew">
      <div class="brew__item"><svg viewBox="0 0 14 14"><circle cx="7" cy="7" r="6" fill="none" stroke="#111" stroke-width="1.2"/><path d="M7 3v4l2 2" fill="none" stroke="#111" stroke-width="1.2"/></svg>3 - 4 Min.</div>
      <div class="brew__item"><svg viewBox="0 0 14 14"><path d="M2 6h9v3a3 3 0 0 1-3 3H5a3 3 0 0 1-3-3z M11 7h1.5v2H11" fill="none" stroke="#111" stroke-width="1.1"/><path d="M5 2v2M8 2v2" stroke="#111" stroke-width="1"/></svg>100°C</div>
      <div class="brew__item"><svg viewBox="0 0 14 14"><ellipse cx="4.5" cy="5" rx="3" ry="2.4" fill="none" stroke="#111" stroke-width="1.1"/><path d="M7 6.5l6 5" stroke="#111" stroke-width="1.3"/></svg>1½ Teesieb</div>
    </div>
    <p class="back__advice">Für optimalen Geschmack<br>weiches Wasser verwenden.</p>
    <p class="back__content">Inhalt: 20g</p>
    <p class="back__dates">Mindestens haltbar bis:<br>Charge:</p>
    <p class="back__maker">Exklusiv für die Teekiste<br>ausgewählt von Teehaus Morgen GmbH<br>Birkenweg 12, D-20000 Hamburg</p>
  </div></div>
  <div class="frame frame--top"><div class="panel top"><p class="top__name">Darjeeling<br>Premium</p><p class="grade">FTGFOP 1<br>First Flush</p></div></div>
  <div class="frame frame--front"><div class="panel front"><p class="front__name">Darjeeling<br>Premium</p><p class="grade">FTGFOP 1<br>First Flush</p><p class="front__share">100 %<br>Schwarzer Tee</p><p class="front__origin">Lindgar Farm im<br>indischen Himalaya</p><p class="front__taste">fein, aromatisch &amp; blumig</p></div></div>
</section>

<section class="label label--moss">
  <div class="label__surface" role="img" aria-label="Decorative pattern area in moss green"></div>
  <div class="frame frame--back"><div class="panel back">
    <div class="brew">
      <div class="brew__item"><svg viewBox="0 0 14 14"><circle cx="7" cy="7" r="6" fill="none" stroke="#111" stroke-width="1.2"/><path d="M7 3v4l2 2" fill="none" stroke="#111" stroke-width="1.2"/></svg>3 - 4 Min.</div>
      <div class="brew__item"><svg viewBox="0 0 14 14"><path d="M2 6h9v3a3 3 0 0 1-3 3H5a3 3 0 0 1-3-3z M11 7h1.5v2H11" fill="none" stroke="#111" stroke-width="1.1"/><path d="M5 2v2M8 2v2" stroke="#111" stroke-width="1"/></svg>100°C</div>
      <div class="brew__item"><svg viewBox="0 0 14 14"><ellipse cx="4.5" cy="5" rx="3" ry="2.4" fill="none" stroke="#111" stroke-width="1.1"/><path d="M7 6.5l6 5" stroke="#111" stroke-width="1.3"/></svg>1½ Teesieb</div>
    </div>
    <p class="back__advice">Für optimalen Geschmack<br>weiches Wasser verwenden.</p>
    <p class="back__content">Inhalt: 20g</p>
    <p class="back__dates">Mindestens haltbar bis:<br>Charge:</p>
    <p class="back__maker">Exklusiv für die Teekiste<br>ausgewählt von Teehaus Morgen GmbH<br>Birkenweg 12, D-20000 Hamburg</p>
  </div></div>
  <div class="frame frame--top"><div class="panel top"><p class="top__name">Darjeeling<br>Premium</p><p class="grade">FTGFOP 1<br>First Flush</p></div></div>
  <div class="frame frame--front"><div class="panel front"><p class="front__name">Darjeeling<br>Premium</p><p class="grade">FTGFOP 1<br>First Flush</p><p class="front__share">100 %<br>Schwarzer Tee</p><p class="front__origin">Lindgar Farm im<br>indischen Himalaya</p><p class="front__taste">fein, aromatisch &amp; blumig</p></div></div>
</section>

<section class="label label--saffron">
  <div class="label__surface" role="img" aria-label="Decorative pattern area in saffron yellow and orange red"></div>
  <div class="frame frame--back"><div class="panel back">
    <div class="brew">
      <div class="brew__item"><svg viewBox="0 0 14 14"><circle cx="7" cy="7" r="6" fill="none" stroke="#111" stroke-width="1.2"/><path d="M7 3v4l2 2" fill="none" stroke="#111" stroke-width="1.2"/></svg>3 - 4 Min.</div>
      <div class="brew__item"><svg viewBox="0 0 14 14"><path d="M2 6h9v3a3 3 0 0 1-3 3H5a3 3 0 0 1-3-3z M11 7h1.5v2H11" fill="none" stroke="#111" stroke-width="1.1"/><path d="M5 2v2M8 2v2" stroke="#111" stroke-width="1"/></svg>100°C</div>
      <div class="brew__item"><svg viewBox="0 0 14 14"><ellipse cx="4.5" cy="5" rx="3" ry="2.4" fill="none" stroke="#111" stroke-width="1.1"/><path d="M7 6.5l6 5" stroke="#111" stroke-width="1.3"/></svg>1½ Teesieb</div>
    </div>
    <p class="back__advice">Für optimalen Geschmack<br>weiches Wasser verwenden.</p>
    <p class="back__content">Inhalt: 20g</p>
    <p class="back__dates">Mindestens haltbar bis:<br>Charge:</p>
    <p class="back__maker">Exklusiv für die Teekiste<br>ausgewählt von Teehaus Morgen GmbH<br>Birkenweg 12, D-20000 Hamburg</p>
  </div></div>
  <div class="frame frame--top"><div class="panel top"><p class="top__name">Darjeeling<br>Premium</p><p class="grade">FTGFOP 1<br>First Flush</p></div></div>
  <div class="frame frame--front"><div class="panel front"><p class="front__name">Darjeeling<br>Premium</p><p class="grade">FTGFOP 1<br>First Flush</p><p class="front__share">100 %<br>Schwarzer Tee</p><p class="front__origin">Lindgar Farm im<br>indischen Himalaya</p><p class="front__taste">fein, aromatisch &amp; blumig</p></div></div>
</section>

<section class="label label--crimson">
  <div class="label__surface" role="img" aria-label="Textured surface in deep crimson and black"></div>
  <div class="frame frame--back"><div class="panel back">
    <div class="brew">
      <div class="brew__item"><svg viewBox="0 0 14 14"><circle cx="7" cy="7" r="6" fill="none" stroke="#111" stroke-width="1.2"/><path d="M7 3v4l2 2" fill="none" stroke="#111" stroke-width="1.2"/></svg>3 - 4 Min.</div>
      <div class="brew__item"><svg viewBox="0 0 14 14"><path d="M2 6h9v3a3 3 0 0 1-3 3H5a3 3 0 0 1-3-3z M11 7h1.5v2H11" fill="none" stroke="#111" stroke-width="1.1"/><path d="M5 2v2M8 2v2" stroke="#111" stroke-width="1"/></svg>100°C</div>
      <div class="brew__item"><svg viewBox="0 0 14 14"><ellipse cx="4.5" cy="5" rx="3" ry="2.4" fill="none" stroke="#111" stroke-width="1.1"/><path d="M7 6.5l6 5" stroke="#111" stroke-width="1.3"/></svg>1½ Teesieb</div>
    </div>
    <p class="back__advice">Für optimalen Geschmack<br>weiches Wasser verwenden.</p>
    <p class="back__content">Inhalt: 20g</p>
    <p class="back__dates">Mindestens haltbar bis:<br>Charge:</p>
    <p class="back__maker">Exklusiv für die Teekiste<br>ausgewählt von Teehaus Morgen GmbH<br>Birkenweg 12, D-20000 Hamburg</p>
  </div></div>
  <div class="frame frame--top"><div class="panel top"><p class="top__name">Darjeeling<br>Premium</p><p class="grade">FTGFOP 1<br>First Flush</p></div></div>
  <div class="frame frame--front"><div class="panel front"><p class="front__name">Darjeeling<br>Premium</p><p class="grade">FTGFOP 1<br>First Flush</p><p class="front__share">100 %<br>Schwarzer Tee</p><p class="front__origin">Lindgar Farm im<br>indischen Himalaya</p><p class="front__taste">fein, aromatisch &amp; blumig</p></div></div>
</section>

<section class="label label--forest">
  <div class="label__surface" role="img" aria-label="Textured surface in dark forest green and black"></div>
  <div class="frame frame--back"><div class="panel back">
    <div class="brew">
      <div class="brew__item"><svg viewBox="0 0 14 14"><circle cx="7" cy="7" r="6" fill="none" stroke="#111" stroke-width="1.2"/><path d="M7 3v4l2 2" fill="none" stroke="#111" stroke-width="1.2"/></svg>3 - 4 Min.</div>
      <div class="brew__item"><svg viewBox="0 0 14 14"><path d="M2 6h9v3a3 3 0 0 1-3 3H5a3 3 0 0 1-3-3z M11 7h1.5v2H11" fill="none" stroke="#111" stroke-width="1.1"/><path d="M5 2v2M8 2v2" stroke="#111" stroke-width="1"/></svg>100°C</div>
      <div class="brew__item"><svg viewBox="0 0 14 14"><ellipse cx="4.5" cy="5" rx="3" ry="2.4" fill="none" stroke="#111" stroke-width="1.1"/><path d="M7 6.5l6 5" stroke="#111" stroke-width="1.3"/></svg>1½ Teesieb</div>
    </div>
    <p class="back__advice">Für optimalen Geschmack<br>weiches Wasser verwenden.</p>
    <p class="back__content">Inhalt: 20g</p>
    <p class="back__dates">Mindestens haltbar bis:<br>Charge:</p>
    <p class="back__maker">Exklusiv für die Teekiste<br>ausgewählt von Teehaus Morgen GmbH<br>Birkenweg 12, D-20000 Hamburg</p>
  </div></div>
  <div class="frame frame--top"><div class="panel top"><p class="top__name">Darjeeling<br>Premium</p><p class="grade">FTGFOP 1<br>First Flush</p></div></div>
  <div class="frame frame--front"><div class="panel front"><p class="front__name">Darjeeling<br>Premium</p><p class="grade">FTGFOP 1<br>First Flush</p><p class="front__share">100 %<br>Schwarzer Tee</p><p class="front__origin">Lindgar Farm im<br>indischen Himalaya</p><p class="front__taste">fein, aromatisch &amp; blumig</p></div></div>
</section>

</main>
</body>
</html>
```